vantoreq realty business card

We need a Business card for our new business. The logo was designed by BrushQuill, and the text We want on the back is:
REAL ESTATE INVESTMENTS
- BUY, RENOVATE, SELL AND RENT RESIDENTIAL PROPERTIES
- FULL HOME REHABBING , REMODELING AND INTERIOR DESIGN
- HOME STAGING SERVICES
- WHOLESALE INVESTOR PROPERTIES
- MAKE CASH OFFERS ON HOUSES IN ANY CONDITION AND IN ANY SITUATION
- PRIVATE MONEY INVESTOR PROGRAMS WITH 6-12% RETURNS
- PAY CASH REWARDS FOR REFFERALS
- CONCIERGE SERVICE

Business

```html
<!DOCTYPE html>
<html lang="en">
<head>
<meta charset="utf-8">
<title>vantoreq Realty – Business Card</title>
<link rel="stylesheet" href="https://fonts.googleapis.com/css2?family=Open+Sans:wght@400;600&family=Arimo:wght@400&display=swap">
<style>
  :root {
    --stage: #b3b0b0;
    --card-white: #ffffff;
    --teal: #5bc3d5;
    --teal-deep: #47b5ca;
    --teal-text: #4fbcd0;
    --grey-text: #6d6e70;
    --grey-light: #8a8b8d;
    --divider: #9a9a9a;
    --on-teal: #ffffff;
    --on-teal-heading: #7b8f94;
  }
  * { box-sizing: border-box; margin: 0; padding: 0; }
  html, body { width: 1200px; height: 900px; overflow: hidden; }
  body {
    background: var(--stage);
    display: flex;
    align-items: center;
    justify-content: center;
    gap: 40px;
    font-family: "Open Sans", sans-serif;
  }
  .card {
    width: 540px;
    height: 310px;
    border-radius: 22px;
    position: relative;
    overflow: hidden;
    box-shadow: 0 14px 26px rgba(0,0,0,0.22);
  }

  /* Front */
  .card--front { background: var(--card-white); }
  .brand {
    position: absolute;
    top: 40px; left: 0; right: 0;
    text-align: center;
  }
  .brand__mark {
    display: block;
    width: 34px; height: 34px;
    margin: 0 auto 16px;
    border: 4px solid var(--grey-light);
  }
  .brand__name {
    font-size: 25px;
    font-weight: 400;
    color: var(--teal-text);
    letter-spacing: 0.3px;
    line-height: 1;
  }
  .brand__tagline {
    margin-top: 6px;
    font-size: 11.5px;
    letter-spacing: 1.2px;
    color: var(--grey-text);
  }
  .band {
    position: absolute;
    top: 158px; left: 0; right: 0;
    height: 7px;
    background: var(--teal);
  }
  .person {
    position: absolute;
    top: 198px; left: 36px;
    width: 190px;
    text-align: right;
  }
  .person__name { font-size: 19px; font-weight: 600; color: var(--teal-text); }
  .person__title { font-size: 10.5px; color: var(--grey-text); margin-top: 1px; }
  .rule {
    position: absolute;
    top: 184px; left: 244px;
    width: 1px; height: 102px;
    background: var(--divider);
  }
  .contacts {
    position: absolute;
    top: 180px; left: 258px;
    list-style: none;
    font-size: 13px;
    font-weight: 600;
    color: var(--grey-text);
    line-height: 17px;
  }
  .contacts li { display: flex; align-items: center; gap: 5px; }
  .contacts svg { width: 12px; height: 12px; flex: none; }
  .contacts .indent { padding-left: 17px; }

  /* Back */
  .card--back {
    background: linear-gradient(180deg, var(--teal) 0%, var(--teal-deep) 100%);
    font-family: "Arimo", sans-serif;
    text-align: center;
    padding-top: 48px;
  }
  .services__heading {
    font-size: 15px;
    letter-spacing: 0.6px;
    color: var(--on-teal-heading);
    margin-bottom: 12px;
  }
  .services__list { list-style: none; color: var(--on-teal); font-size: 11.6px; letter-spacing: 0.3px; }
  .services__list li { line-height: 25px; }
  .back-mark {
    position: absolute;
    right: 26px; bottom: 46px;
    width: 32px; height: 32px;
    border: 3px solid var(--on-teal);
  }
</style>
</head>
<body>
  <section class="card card--front">
    <div class="brand">
      <span class="brand__mark"></span>
      <div class="brand__name">VANTOREQ Realty</div>
      <div class="brand__tagline">REAL ESTATE SOLUTIONS</div>
    </div>
    <div class="band"></div>
    <div class="person">
      <div class="person__name">Marcus Whitfield</div>
      <div class="person__title">Executive Director</div>
    </div>
    <div class="rule"></div>
    <ul class="contacts">
      <li><svg viewBox="0 0 12 12"><rect x="3" y="0.5" width="6" height="11" rx="1.2" fill="none" stroke="#5bc3d5" stroke-width="1.4"/><line x1="5" y1="9.5" x2="7" y2="9.5" stroke="#5bc3d5" stroke-width="1.2"/></svg>555-201-1545</li>
      <li><svg viewBox="0 0 12 12"><path d="M2.5 1 L4.5 1 L5.3 3.6 L4 4.6 Q5 7 7.4 8 L8.4 6.7 L11 7.5 L11 9.5 Q10.5 11 9 11 Q2 10 1 3 Q1 1.5 2.5 1 Z" fill="#5bc3d5"/></svg>555-201-7220</li>
      <li><svg viewBox="0 0 12 12"><rect x="1" y="4" width="10" height="7" rx="1" fill="none" stroke="#5bc3d5" stroke-width="1.3"/><rect x="3" y="1" width="6" height="4" fill="none" stroke="#5bc3d5" stroke-width="1.2"/><rect x="3.5" y="7" width="5" height="1.5" fill="#5bc3d5"/></svg>555-201-9421</li>
      <li><svg viewBox="0 0 12 12"><rect x="0.8" y="2.3" width="10.4" height="7.4" fill="none" stroke="#5bc3d5" stroke-width="1.3"/><path d="M1 2.6 L6 6.6 L11 2.6" fill="none" stroke="#5bc3d5" stroke-width="1.2"/></svg>marcus@vantoreqrealty.com</li>
      <li><svg viewBox="0 0 12 12"><circle cx="6" cy="6" r="5" fill="none" stroke="#5bc3d5" stroke-width="1.2"/><ellipse cx="6" cy="6" rx="2.2" ry="5" fill="none" stroke="#5bc3d5" stroke-width="1"/><line x1="1" y1="6" x2="11" y2="6" stroke="#5bc3d5" stroke-width="1"/></svg>www.vantoreqrealty.com</li>
      <li><svg viewBox="0 0 12 12"><path d="M6 0.8 L11.4 6 L9.8 6 L9.8 11 L2.2 11 L2.2 6 L0.6 6 Z" fill="#5bc3d5"/></svg>418 W. Elm Street</li>
      <li class="indent">PO Box 310 Millbrook, NC 27999</li>
    </ul>
  </section>

  <section class="card card--back">
    <h2 class="services__heading">REAL ESTATE INVESTMENTS</h2>
    <ul class="services__list">
      <li>BUY, RENOVATE, SELL AND RENT RESIDENTIAL PROPERTIES</li>
      <li>FULL HOME REHABBING , REMODELING AND INTERIOR DESIGN</li>
      <li>HOME STAGING SERVICES</li>
      <li>WHOLESALE INVESTOR PROPERTIES</li>
      <li>MAKE CASH OFFERS ON HOUSES IN ANY CONDITION AND IN ANY SITUATION</li>
      <li>PRIVATE MONEY INVESTOR PROGRAMS WITH 6-12% RETURNS</li>
      <li>PAY CASH REWARDS FOR REFFERALS</li>
      <li>CONCIERGE SERVICE</li>
    </ul>
    <span class="back-mark"></span>
  </section>
</body>
</html>
```